BrickaFun Business Card

We need a business card design for our company. We sell construction-themed amusement rides for kids.

Contact Information for Business Card

Contact info on business card should include:
Dale Hurst
Co-Founder & COO
(833) 517-BRICKAF
Dale@brickafun.com
www.brickafun.com

```html
<!DOCTYPE html>
<html lang="en">
<head>
<meta charset="utf-8">
<title>BrickaFun Business Card</title>
<link rel="stylesheet" href="https://fonts.googleapis.com/css2?family=Russo+One&family=Exo+2:wght@400;500;700&display=swap">
<style>
  :root {
    --stage: #1c1c1c;
    --card: #0b0b0b;
    --orange: #f07a26;
    --orange-red: #ee5a1f;
    --amber: #f39a1e;
    --rule: #d9d9d9;
    --accent-blue: #2aa8e6;
    --hat-yellow: #f2c230;
    --vest-orange: #e8672a;
    --jeans-blue: #2a3f7a;
    --shirt-white: #e6e6e6;
    --trouser-grey: #7a7a7a;
  }
  * { box-sizing: border-box; margin: 0; padding: 0; }
  html, body { width: 1200px; height: 900px; overflow: hidden; }
  body {
    background: var(--stage);
    position: relative;
    font-family: "Exo 2", sans-serif;
  }
  .card {
    position: absolute;
    left: 240px;
    width: 720px;
    height: 405px;
    background: var(--card);
    box-shadow: 0 10px 30px rgba(0,0,0,0.6);
    overflow: hidden;
  }
  .card--back { top: 30px; }
  .card--front { top: 465px; }

  .crew-figure {
    position: absolute;
    border-radius: 60px 60px 10px 10px;
  }
  .crew-figure--left {
    left: 195px;
    top: 55px;
    width: 130px;
    height: 320px;
    background: linear-gradient(180deg, var(--hat-yellow) 0%, var(--hat-yellow) 18%, #e9b48e 28%, var(--vest-orange) 45%, var(--jeans-blue) 70%, #1e2c58 100%);
  }
  .crew-figure--right {
    left: 385px;
    top: 80px;
    width: 150px;
    height: 310px;
    background: linear-gradient(180deg, var(--hat-yellow) 0%, var(--hat-yellow) 18%, #e9b48e 30%, var(--shirt-white) 48%, var(--vest-orange) 62%, var(--trouser-grey) 78%, #555 100%);
  }

  .brand-name {
    position: absolute;
    left: 60px;
    top: 48px;
    font-family: "Russo One", sans-serif;
    font-size: 84px;
    line-height: 1.2;
    color: var(--orange);
  }
  .divider {
    position: absolute;
    left: 60px;
    right: 60px;
    top: 205px;
    height: 2px;
    background: var(--rule);
  }
  .contact-list {
    position: absolute;
    left: 60px;
    top: 252px;
    list-style: none;
    color: var(--amber);
    font-size: 21px;
    line-height: 34px;
  }
  .contact-list li { display: flex; align-items: center; gap: 10px; }
  .contact-list svg { width: 20px; height: 20px; flex: none; stroke: var(--orange-red); fill: none; stroke-width: 1.8; }
  .contact-list strong { font-weight: 700; }

  .person {
    position: absolute;
    right: 60px;
    top: 282px;
    text-align: right;
  }
  .person__name {
    font-family: "Russo One", sans-serif;
    font-size: 38px;
    color: var(--orange-red);
    line-height: 1;
  }
  .person__title {
    font-size: 22px;
    color: var(--amber);
    margin-top: 8px;
  }
  .accent-bar {
    position: absolute;
    right: 22px;
    top: 285px;
    width: 8px;
    height: 70px;
    background: var(--accent-blue);
  }
</style>
</head>
<body>
  <section class="card card--back">
    <div class="crew-figure crew-figure--left" role="img" aria-label="Cartoon female construction worker in a yellow hard hat, orange shirt and blue overalls with arms crossed"></div>
    <div class="crew-figure crew-figure--right" role="img" aria-label="Cartoon male construction worker in a yellow hard hat, white shirt and orange safety vest with arms crossed"></div>
  </section>

  <section class="card card--front">
    <div class="brand-name">BrickaFun</div>
    <div class="divider"></div>
    <ul class="contact-list">
      <li>
        <svg viewBox="0 0 24 24"><path d="M5 3h4l2 5-3 2a12 12 0 0 0 6 6l2-3 5 2v4a2 2 0 0 1-2 2A18 18 0 0 1 3 5a2 2 0 0 1 2-2z"/></svg>
        <span>(833) 517-BRICKAF</span>
      </li>
      <li>
        <svg viewBox="0 0 24 24"><rect x="3" y="5" width="18" height="14" rx="1"/><path d="M3 6l9 7 9-7"/></svg>
        <span>Dale@brickafun.com</span>
      </li>
      <li>
        <svg viewBox="0 0 24 24"><circle cx="12" cy="12" r="9"/><path d="M3 12h18M12 3c3 3 3 15 0 18M12 3c-3 3-3 15 0 18"/></svg>
        <span>www.<strong>brickafun</strong>.com</span>
      </li>
    </ul>
    <div class="person">
      <div class="person__name">Dale Hurst</div>
      <div class="person__title">Co-Founder &amp; COO</div>
    </div>
    <div class="accent-bar"></div>
  </section>
</body>
</html>
```